Gourmet food made with love and care in my country kitchen

I'd like a business card designed for my small home-based food business. I have made labelling in federation blue for my food products (Labneh cheese, spicy pumpkin chutney, dukkah, caramelised onion jam, yo-Yo biscuits, chocolate mud cake etc) and have navy and white checked surrounds/borders on my brochures so would like to stick to these country colours.
Target Market(s)
Foodies who love gourmet delicacies. Everyone who enjoys a picnic that they don't have to prepare themselves.
Industry/Entity Type
Business
Contact Information for Business Card
Larkhollow Pantry
42 Tindale's Lane
Brimsworth Qld 4829
Phone Viv 07 48216597 or 0412386951
- Harrington

```html
<!DOCTYPE html>
<html lang="en">
<head>
<meta charset="utf-8">
<title>Larkhollow Pantry – Business Card</title>
<link href="https://fonts.googleapis.com/css2?family=Open+Sans:ital,wght@0,400;0,600;1,400&display=swap" rel="stylesheet">
<style>
  :root {
    --federation-blue: #0a56a4;
    --navy: #0c3a78;
    --ink-blue: #1e4fa0;
    --pale-blue: #c9d8ee;
    --white: #ffffff;
    --ink: #1a1a1a;
    --backdrop: #efece6;
    --photo-light: #9db8cf;
    --photo-deep: #587f44;
  }
  * { margin: 0; padding: 0; box-sizing: border-box; }
  html, body { width: 1000px; height: 1200px; overflow: hidden; }
  body {
    position: relative;
    background: var(--backdrop);
    font-family: "Open Sans", Arial, sans-serif;
  }
  .card {
    position: absolute;
    left: 105px;
    width: 792px;
    height: 488px;
    overflow: hidden;
  }
  .card-front { top: 45px; background: var(--white); }
  .card-back { top: 620px; background: var(--federation-blue); color: var(--white); }

  /* Front */
  .front-art { position: absolute; inset: 0; }
  .brand-band {
    position: absolute;
    left: 0; top: 142px;
    width: 460px; height: 70px;
    background: linear-gradient(90deg, rgba(201,216,238,0) 0%, var(--pale-blue) 18%, var(--pale-blue) 70%, rgba(201,216,238,0) 100%);
  }
  .brand-name {
    position: absolute;
    left: 90px; top: 118px;
    width: 300px;
    text-align: center;
    font-size: 40px;
    line-height: 46px;
    font-weight: 400;
    color: var(--ink-blue);
  }
  .offer-list {
    position: absolute;
    left: 90px; top: 268px;
    width: 300px;
    list-style: none;
    text-align: center;
    color: var(--ink-blue);
    font-size: 19px;
    line-height: 31px;
  }
  .offer-list li svg { width: 15px; height: 13px; margin-right: 8px; vertical-align: 0; }
  .owner-note {
    position: absolute;
    left: 30px; top: 383px;
    width: 420px;
    text-align: center;
    font-style: italic;
    font-size: 17.5px;
    line-height: 21px;
    color: var(--ink);
  }

  /* Back */
  .title-rule {
    position: absolute;
    top: 183px;
    height: 25px;
    background: linear-gradient(var(--navy) 0 12px, var(--white) 12px 25px);
  }
  .title-rule.left { left: 0; width: 143px; }
  .title-rule.right { left: 578px; width: 214px; }
  .back-title {
    position: absolute;
    left: 153px; top: 164px;
    font-size: 48px;
    line-height: 56px;
    font-weight: 400;
    white-space: nowrap;
  }
  .address {
    position: absolute;
    left: 153px; top: 224px;
    font-size: 21px;
    letter-spacing: 1px;
  }
  .contact-list {
    position: absolute;
    left: 153px; top: 254px;
    list-style: none;
    font-size: 18px;
    letter-spacing: 0.8px;
  }
  .contact-list li { display: flex; align-items: center; height: 36.5px; }
  .contact-list svg, .contact-list .icon-space { width: 30px; height: 30px; margin-right: 13px; flex: none; }
</style>
</head>
<body>

<section class="card card-front" aria-label="Business card front">
  <svg class="front-art" width="792" height="488" viewBox="0 0 792 488">
    <defs>
      <linearGradient id="photoTones" x1="0" y1="0" x2="0.4" y2="1">
        <stop offset="0" stop-color="var(--photo-light)"/>
        <stop offset="1" stop-color="var(--photo-deep)"/>
      </linearGradient>
    </defs>
    <polygon points="432,0 448,0 565,488 548,488" fill="var(--federation-blue)"/>
    <polygon points="446,0 792,0 792,488 562,488" fill="url(#photoTones)" role="img" aria-label="Photo of a savoury tomato tart and a bottle of olive oil on an outdoor table overlooking green cane fields and trees"/>
  </svg>
  <div class="brand-band"></div>
  <h1 class="brand-name">Larkhollow<br>Pantry</h1>
  <ul class="offer-list">
    <li><svg viewBox="0 0 15 13"><path d="M1 7 L5.5 11.5 L14 1.5" fill="none" stroke="currentColor" stroke-width="3"/></svg>Gourmet Market Food</li>
    <li><svg viewBox="0 0 15 13"><path d="M1 7 L5.5 11.5 L14 1.5" fill="none" stroke="currentColor" stroke-width="3"/></svg>Vintage Picnic Hampers</li>
    <li><svg viewBox="0 0 15 13"><path d="M1 7 L5.5 11.5 L14 1.5" fill="none" stroke="currentColor" stroke-width="3"/></svg>Cooking Classes</li>
  </ul>
  <p class="owner-note">Gourmet food made in my country kitchen,<br>using fresh ingredients, for your enjoyment<br>and convenience. Viv Marsh</p>
</section>

<section class="card card-back" aria-label="Business card back">
  <div class="title-rule left"></div>
  <div class="title-rule right"></div>
  <h2 class="back-title">Larkhollow Pantry</h2>
  <p class="address">42 Tindale's Lane, Mt Orrin Via Brimsworth</p>
  <ul class="contact-list">
    <li>
      <svg viewBox="0 0 30 30" aria-hidden="true">
        <circle cx="15" cy="15" r="14" fill="var(--white)"/>
        <path d="M11 7 C8 9 8 13 10 17 C12 21 15 24 19 24 L21 21 L18 18.5 L16.5 20 C14.5 19 12.5 16.5 12 14 L13.5 12.5 L12.5 8 Z" fill="var(--federation-blue)"/>
      </svg>
      07 48216597 or 0412386951
    </li>
    <li>
      <svg viewBox="0 0 30 30" aria-hidden="true">
        <circle cx="15" cy="15" r="14" fill="var(--white)"/>
        <rect x="7" y="9.5" width="16" height="11" fill="none" stroke="var(--federation-blue)" stroke-width="2"/>
        <path d="M7 9.5 L15 16 L23 9.5" fill="none" stroke="var(--federation-blue)" stroke-width="2"/>
      </svg>
      larkhollowpantry@postmail.com
    </li>
    <li>
      <span class="icon-space" aria-hidden="true"></span>
      Larkhollow Pantry
    </li>
  </ul>
</section>

</body>
</html>
```